Figure for Manufacture of Wound Healing Gel

Who we are: We are a nationally funded bioengineering laboratory at Harlow Ridge University conducting research on the tendon healing properties of a gel manufactured from real tendon.

What we need: We require a figure piece that will be included in an academic publication. With that in mind, the figure must be professional, clear, and concise. A reader would need to glance at the figure for only a moment to understand the process of how we manufacture and store tendon gel. Actual pictures of the in-between steps are included and will need to be cropped to improve the professional look of the design.

The Details: The figure should stepwise show the process of how we manufacture and store tendon gel. In brief, we harvest tendon from donor cadavers. Those tendons undergo decellularization, lyophilization (fancy word for freeze-drying), and are milled into a fine powder. The powder is set in acidified water and treated with digestive enzymes. After 24 hrs, the gel is brought to physiologic pH and salinity and placed in vials. The vials are frozen and again lyophilized (this is so they can be stored and transported easily). Finally the samples are reconstituted with DI water.

The Figure: Should be a linear process (horizontal). The following are the actual steps we wish to include (steps need not be numbered necessarily as long as they are in logical order...

1.) A picture of harvested tendon (Step 1.jpg)
2.) Written description: "Decellularization, lyophilization, and milling"
3.) A picture of milled tendon powder (Step 2.jpg)
4.) Written description: "Digestion with pepsin before establishing physiologic pH and salinity".
5.) A picture of gel (Step 3.jpg)
6.) Written description: "Lyophilization of aliquots"
7.) A picture of freeze-dried gel (Step 4.jpg)
8.) Written description: "Reconstitution with DI water"
9.) A picture of reconstituted gel (Step 5.jpg)

Feel free to message for any questions, comments, or clarifications.

```html
<!DOCTYPE html>
<html lang="en">
<head>
<meta charset="UTF-8">
<title>Tendon Gel Manufacture and Storage</title>
<link href="https://fonts.googleapis.com/css2?family=Archivo+Black&family=Roboto:wght@400&display=swap" rel="stylesheet">
<style>
  :root {
    --paper: #f1f1f1;
    --ink: #1d1d1d;
    --blue-deep: #0b2458;
    --blue-mid: #15469a;
    --blue-glow: #2a78d2;
    --card: #ffffff;
    --caption: #ffffff;
  }
  * { margin: 0; padding: 0; box-sizing: border-box; }
  html, body { width: 1200px; height: 927px; overflow: hidden; background: #ffffff; }
  .figure { position: relative; width: 1200px; height: 927px; }
  .title-band {
    position: absolute; left: 0; top: 0; width: 1200px; height: 216px;
    background: var(--paper);
  }
  .title {
    position: absolute; left: 52px; top: 46px;
    font-family: "Archivo Black", sans-serif;
    font-size: 58px; line-height: 62px; color: var(--ink);
    letter-spacing: 0.5px; text-transform: uppercase;
  }
  .process-field {
    position: absolute; left: 0; top: 216px; width: 1200px; height: 711px;
    background:
      radial-gradient(ellipse 60% 45% at 55% 40%, rgba(42,120,210,0.55), transparent 70%),
      radial-gradient(ellipse 30% 30% at 90% 70%, rgba(42,120,210,0.4), transparent 70%),
      linear-gradient(180deg, var(--blue-mid) 0%, var(--blue-deep) 100%);
  }
  .step-card {
    position: absolute; top: 362px; width: 192px; height: 308px;
    background: var(--card); padding: 5px;
  }
  .step-photo { width: 182px; height: 242px; }
  .photo-tendon { background: linear-gradient(160deg, #8b8b86 0%, #d9d2bd 45%, #7d7f80 100%); }
  .photo-powder { background: radial-gradient(ellipse at 50% 40%, #e8dfb8 0%, #b9b5a3 45%, #6f7274 100%); }
  .photo-gel { background: radial-gradient(ellipse at 50% 45%, #e6e9ea 0%, #a3a9ad 40%, #55595d 100%); }
  .photo-vial-dry { background: radial-gradient(ellipse at 50% 55%, #d8d2c3 0%, #4a4a4a 30%, #1b1b1b 100%); }
  .photo-vial-wet { background: radial-gradient(ellipse at 50% 60%, #e4dfcf 0%, #4c4c4c 30%, #1b1b1b 100%); }
  .step-arrow { position: absolute; top: 468px; width: 66px; height: 58px; }
  .step-caption {
    position: absolute; top: 712px; width: 200px;
    font-family: "Roboto", sans-serif; font-size: 15px; line-height: 17px;
    color: var(--caption); text-align: center;
  }
</style>
</head>
<body>
<div class="figure">
  <div class="title-band">
    <h1 class="title">The process of manufacture<br>and store tendon gel</h1>
  </div>
  <div class="process-field"></div>

  <div class="step-card" style="left:38px"><div class="step-photo photo-tendon" role="img" aria-label="Harvested tendon in a glass dish"></div></div>
  <div class="step-card" style="left:273px"><div class="step-photo photo-powder" role="img" aria-label="Milled tendon powder in a glass dish"></div></div>
  <div class="step-card" style="left:508px"><div class="step-photo photo-gel" role="img" aria-label="Tendon gel in a glass dish"></div></div>
  <div class="step-card" style="left:743px"><div class="step-photo photo-vial-dry" role="img" aria-label="Freeze-dried gel in a capped vial"></div></div>
  <div class="step-card" style="left:978px"><div class="step-photo photo-vial-wet" role="img" aria-label="Reconstituted gel in a capped vial"></div></div>

  <svg class="step-arrow" style="left:218px" viewBox="0 0 66 58"><polygon points="0,16 36,16 36,0 66,29 36,58 36,42 0,42" fill="#fff"/></svg>
  <svg class="step-arrow" style="left:453px" viewBox="0 0 66 58"><polygon points="0,16 36,16 36,0 66,29 36,58 36,42 0,42" fill="#fff"/></svg>
  <svg class="step-arrow" style="left:688px" viewBox="0 0 66 58"><polygon points="0,16 36,16 36,0 66,29 36,58 36,42 0,42" fill="#fff"/></svg>
  <svg class="step-arrow" style="left:923px" viewBox="0 0 66 58"><polygon points="0,16 36,16 36,0 66,29 36,58 36,42 0,42" fill="#fff"/></svg>

  <p class="step-caption" style="left:34px">Decellularization,<br>lyophilization,<br>and milling</p>
  <p class="step-caption" style="left:269px">Digestion with pepsin<br>before establishing<br>physiologic pH<br>and salinity</p>
  <p class="step-caption" style="left:504px">Lyophilization<br>of aliquots</p>
  <p class="step-caption" style="left:739px">Reconstitution<br>with DI water</p>
</div>
</body>
</html>
```